Design a Consultation and HR Services Website "Shift Pathways"

Consultation and HR Services
I am looking for a design gives the look and feel of Varden Calloway and Ferrovane
we need a high-quality graphics website that looks rich and expensive.
we are working as an affiliate for international consultation firms and sole agent for international HR products.
we are a group of consultants for the Middle East.
we will get the global practices to local practices.

Reason: I am not getting enough options and designs. I am not getting what I was looking for in matter of look and feel. looking for something rich and luxury with black background and rich font. www.blockvault.example www.lucindavarga.example 71dormerplace.example/ www.velquo.example/rd/en/ morvethhouse.example/ www.velquo.example/rd/en/ www.quillen.example/ www.theplaudits.example/ .

Target Market(s)

Corporate all size and industries in GCC

Industry/Entity Type

Management Consulting

Coding

Coded - Design and coding required

Number of Pages Required

5+ page

Font styles to use
Sans Serif
Script

Colors
ffffff
ecf7fb
cee9f5
85cae6
33a6d7
0592cd
000000
848484

Requirements
Must have
• This is the looks and feel that I'm looking for.
• http://www.blockvault.example/?channel=display&subchannel=sitemuse
• http://www.lucindavarga.example/lvny-private/en/
• http://71dormerplace.example/
• http://www.velquo.example/rd/en/
• http://morvethhouse.example/
• http://www.quillen.example/
• http://www.theplaudits.example/
• Home
• Who we are?
• What we do?
• HR & OD Consultation
• Executive Coaching
• Assesment Cemter
• HRIS & Outsourcing
• Testimonials
• Our Partners
• Contact Us
• We need support on Technical righting...

```html
<!DOCTYPE html>
<html lang="en">
<head>
<meta charset="utf-8">
<title>Shift Pathways — Consultation and HR Services</title>
<link href="https://fonts.googleapis.com/css2?family=Arimo:ital,wght@0,400;0,700;1,400&family=Open+Sans:wght@400;600;700&display=swap" rel="stylesheet">
<style>
:root{
  --white:#ffffff;
  --ice:#ecf7fb;
  --frost:#cee9f5;
  --sky:#85cae6;
  --blue:#33a6d7;
  --deep-blue:#0592cd;
  --ink:#2b2b2b;
  --text:#555555;
  --grey:#848484;
  --nav:#8f8f8f;
  --footer:#8b8b8b;
  --soft:#f1f5f7;
}
*{box-sizing:border-box;margin:0;padding:0}
html,body{width:1200px;height:2267px;overflow:hidden;background:var(--white)}
body{position:relative;font-family:"Open Sans",Arial,sans-serif;color:var(--text)}
.abs{position:absolute}

/* header */
.brand{left:98px;top:62px;display:flex;align-items:center;gap:10px}
.brand-mark{width:22px;height:22px;background:var(--blue)}
.brand-name{font-family:"Arimo",Arial,sans-serif;font-size:23px;font-weight:700;color:var(--deep-blue)}
.search{left:660px;top:42px;width:262px;height:43px;border:1px solid #cfcfcf;border-radius:4px;font-size:12px;color:#9a9a9a;padding:14px 16px;letter-spacing:.5px}
.search svg{position:absolute;right:14px;top:13px}
.call{left:961px;top:40px;font-family:"Arimo",Arial,sans-serif;font-size:14px;color:var(--grey);letter-spacing:.5px}
.call-number{left:961px;top:61px;font-family:"Arimo",Arial,sans-serif;font-size:20px;font-weight:700;color:var(--deep-blue)}

.nav{left:0;top:125px;width:1200px;height:51px;background:var(--nav)}
.nav ul{list-style:none;position:absolute;left:98px;top:0;display:flex;border-left:1px solid #a7a7a7}
.nav li{width:167px;height:51px;line-height:51px;text-align:center;color:var(--white);font-family:"Arimo",Arial,sans-serif;font-weight:700;font-size:14px;border-right:1px solid #a7a7a7}

/* hero */
.hero{left:0;top:176px;width:1200px;height:509px;background:linear-gradient(90deg,#eef2f5 0%,#e3e9ee 40%,#c3ced8 58%,#45566b 76%,#6b7a8c 86%,#c9a994 100%)}
.hero-title{left:98px;top:336px;font-family:"Arimo",Arial,sans-serif;font-size:32px;font-weight:700;color:var(--ink)}
.hero-sub{left:98px;top:376px;font-family:"Arimo",Arial,sans-serif;font-size:21px;font-style:italic;color:var(--deep-blue)}
.hero-text{left:98px;top:413px;width:510px;font-size:12.5px;line-height:22px;color:#555}
.btn{background:linear-gradient(#3fb2e0,#1f93c7);color:var(--white);font-weight:700;font-size:13px;text-align:center;border-radius:2px}
.hero-btn{left:98px;top:480px;width:126px;height:40px;line-height:40px}
.dots{display:flex;gap:5px}
.dots span{width:11px;height:11px;border-radius:50%;background:#b9b9b9}
.dots span.on{background:var(--blue)}
.hero-dots{left:568px;top:645px}

/* tweet bar */
.tweet-bar{left:0;top:685px;width:766px;height:56px;background:var(--soft)}
.tweet-icon{left:100px;top:701px;width:24px;height:24px;border-radius:50%;background:var(--blue)}
.tweet-text{left:145px;top:704px;font-size:12px;color:#555}

/* consultation form */
.consult{left:766px;top:685px;width:336px;height:512px;background:var(--soft);border:1px solid #dfe5e8}
.consult-head{height:56px;background:var(--deep-blue);color:var(--white);font-family:"Arimo",Arial,sans-serif;font-size:18px;text-align:center;line-height:56px}
.field{position:absolute;left:13px;width:310px;height:33px;background:var(--white);border:1px solid #dcdcdc;font-size:12px;color:#666;padding:8px 14px}
.field.select svg{position:absolute;right:0;top:0}
.field.area{height:71px}
.consult-submit{position:absolute;left:13px;top:454px;width:310px;height:41px;line-height:41px;font-size:14px}

/* welcome */
.section-title{font-family:"Arimo",Arial,sans-serif;font-size:18px;font-weight:700;color:var(--ink)}
.welcome-title{left:98px;top:791px}
.welcome-photo{left:98px;top:843px;width:243px;height:188px;background:linear-gradient(135deg,#dfe8ee,#8fa3b5 60%,#4a5868)}
.body-copy{font-size:12px;line-height:23px;color:#555;letter-spacing:-.1px}
.welcome-side{left:370px;top:838px;width:358px}
.welcome-side p+p{margin-top:23px}
.welcome-full{left:98px;top:1062px;width:630px}
.read-more{font-size:13px;font-weight:700;color:var(--deep-blue)}
.welcome-more{left:98px;top:1151px}

/* services band */
.services{left:0;top:1241px;width:1200px;height:344px;background:linear-gradient(120deg,#4fb3dc,#2d98c8 55%,#3ea7d4)}
.services-title{left:0;top:1272px;width:1200px;text-align:center;font-family:"Arimo",Arial,sans-serif;font-size:18px;font-weight:700;color:var(--white)}
.service{top:1328px;width:190px;text-align:center;color:var(--white)}
.service svg{display:block;margin:0 auto}
.service h3{font-family:"Arimo",Arial,sans-serif;font-size:14px;font-weight:700;margin-top:10px}
.service p{font-size:12px;line-height:21px;margin-top:6px}
.service .more{font-size:13px;font-weight:700;margin-top:9px}

/* testimonials */
.testi-title{left:98px;top:1625px}
.quote{left:98px;top:1671px;width:500px;height:119px;border:1px solid #cfd4d7;padding:18px 18px;font-size:12px;line-height:26px;font-style:italic;color:#555}
.quote b{color:var(--deep-blue);font-style:normal;font-size:18px}
.avatar{left:106px;top:1838px;width:86px;height:86px;border-radius:50%;background:linear-gradient(#c7d2da,#7c8c99)}
.client{left:219px;top:1871px;font-size:14px;font-weight:700;color:var(--deep-blue)}
.testi-dots{left:130px;top:1937px}

/* news */
.news-title{left:669px;top:1625px}
.news-arrows{left:1068px;top:1625px}
.news-item{left:669px;width:440px;height:76px}
.news-thumb{position:absolute;left:0;top:0;width:95px;height:76px;background:linear-gradient(135deg,#e4ebf0,#8795a3)}
.news-link{position:absolute;left:124px;top:0;width:310px;font-size:12px;line-height:21px;color:#333;text-decoration:underline}
.news-meta{position:absolute;left:124px;top:48px;font-size:12px;color:var(--deep-blue);display:flex;align-items:center;gap:6px}

/* footer */
.footer{left:0;top:1995px;width:1200px;height:272px;background:var(--footer);color:var(--white)}
.f-title{font-family:"Arimo",Arial,sans-serif;font-size:15px;font-weight:700;color:var(--white);top:2020px}
.f-text{font-size:12px;line-height:21px;color:#f3f3f3}
.f-links{list-style:none;font-size:12px;line-height:21.5px;color:#f3f3f3}
.f-input{left:542px;top:2107px;width:255px;height:31px;background:var(--white);font-size:12px;color:#777;padding:7px 12px}
.f-btn{left:542px;top:2150px;width:82px;height:31px;line-height:31px;font-size:11px}
.f-contact{display:flex;gap:16px;align-items:flex-start;font-size:12px;line-height:21px;color:#f3f3f3}
.f-rule{left:98px;top:2209px;width:1002px;height:1px;background:#a3a3a3}
.copyright{left:98px;top:2230px;font-size:12px;color:#f3f3f3}
.social{left:990px;top:2229px;display:flex;gap:9px}
.social span{width:19px;height:19px;background:#f3f3f3;border-radius:3px}
</style>
</head>
<body>

<header>
  <div class="abs brand"><span class="brand-mark"></span><span class="brand-name">Shift Pathways</span></div>
  <div class="abs search">SEARCH..
    <svg width="16" height="16" viewBox="0 0 16 16"><circle cx="6.5" cy="6.5" r="4.5" fill="none" stroke="#888" stroke-width="2"/><line x1="10" y1="10" x2="14" y2="14" stroke="#888" stroke-width="2"/></svg>
  </div>
  <div class="abs call">CALL US TODAY !</div>
  <div class="abs call-number">1 800 555 0142</div>
</header>

<nav class="abs nav">
  <ul><li>HOME</li><li>ABOUT US</li><li>SERVICES</li><li>RESOURCES</li><li>CAREERS</li><li>CONTACT US</li></ul>
</nav>

<section>
  <div class="abs hero" role="img" aria-label="Office photo of two smiling colleagues reviewing a tablet beside a laptop"></div>
  <h1 class="abs hero-title">SHIFT PATHWAYS</h1>
  <p class="abs hero-sub">We are a Consultation and HR Services company</p>
  <p class="abs hero-text">Nemo enim ipsam voluptatem quia voluptas sit aspernatur aut odit aut fugit, sed quia consequuntur magni dolores eos qui ratione voluptatem..</p>
  <div class="abs btn hero-btn">READ MORE &gt;&gt;</div>
  <div class="abs dots hero-dots"><span class="on"></span><span></span><span></span><span></span></div>
</section>

<div class="abs tweet-bar"></div>
<div class="abs tweet-icon"></div>
<p class="abs tweet-text">Nemo enim ipsam voluptatem quia voluptas sit aspernatur aut odit a..John &nbsp;@Shift Pathways &nbsp;#w...</p>

<aside class="abs consult">
  <div class="consult-head">REQUEST A CONSULTATION</div>
  <div class="field" style="top:70px">Name :</div>
  <div class="field" style="top:113px">Email :</div>
  <div class="field" style="top:156px">Phone Number :</div>
  <div class="field" style="top:199px">Title :</div>
  <div class="field" style="top:242px">Phone Number :</div>
  <div class="field" style="top:285px">Company Name :</div>
  <div class="field select" style="top:328px">Select Country :
    <svg width="31" height="31" viewBox="0 0 31 31"><rect width="31" height="31" fill="#ececec"/><path d="M11 13h9l-4.5 5z" fill="#999"/></svg>
  </div>
  <div class="field area" style="top:371px">How Can we Help you ?</div>
  <div class="btn consult-submit">SUBMIT</div>
</aside>

<section>
  <h2 class="abs section-title welcome-title">WELCOME TO SHIFT PATHWAYS</h2>
  <div class="abs welcome-photo" role="img" aria-label="Photo of three colleagues gathered around a laptop"></div>
  <div class="abs body-copy welcome-side">
    <p>On the other hand, we denounce with righteous indignation and dislike men who are so beguiled and demora liz ed by the charms of pleasure of the moment, so blinded by desire, that they cannot foresee the pain Trouble that are bound to ensue; and equal blame belongs shrinking.</p>
    <p>when nothing prevents our being able to do what we like best. These cases are perfectly simple and easy to distinguish. In a free hour, when our power of choice is untrammelled and man</p>
  </div>
  <p class="abs body-copy welcome-full">when nothing prevents our being able to do what we like best, every pleasure is to be welcomed and every pain avoided. But in certain circumstances and owing to the claims of duty or the obligations of business it will frequ ently occur that pleasures have to be repudiated and annoyances accepted.</p>
  <div class="abs read-more welcome-more">READ MORE &gt;&gt;</div>
</section>

<section>
  <div class="abs services"></div>
  <h2 class="abs services-title">SHIFT PATHWAYS CONSULTING SERVICES</h2>

  <div class="abs service" style="left:103px">
    <svg width="104" height="112" viewBox="0 0 104 112"><path d="M52 4a48 48 0 0 1 12 94.5L52 110 40 98.5A48 48 0 0 1 52 4z" fill="#fff"/><circle cx="52" cy="52" r="43" fill="#2f9dcc"/><path d="M52 30a13 13 0 0 0-7 24v6h14v-6a13 13 0 0 0-7-24z M46 64h12 M47 69h10" fill="none" stroke="#fff" stroke-width="3"/></svg>
    <h3>TALENT ORGANIZATION</h3><p>Nam libero tempore, cum soln obis est eligendi optio cum</p><div class="more">READ MORE&gt;&gt;</div>
  </div>
  <div class="abs service" style="left:305px">
    <svg width="104" height="112" viewBox="0 0 104 112"><path d="M52 4a48 48 0 0 1 12 94.5L52 110 40 98.5A48 48 0 0 1 52 4z" fill="#fff"/><circle cx="52" cy="52" r="43" fill="#2f9dcc"/><circle cx="52" cy="52" r="19" fill="#fff"/><path d="M40 46q8-4 10 4t8 2q6-2 10 4M44 62q6-2 8 4" fill="none" stroke="#2f9dcc" stroke-width="3"/></svg>
    <h3>GLOBALIZATION</h3><p>Nam libero tempore, cum soln obis est eligendi optio cum</p><div class="more">READ MORE&gt;&gt;</div>
  </div>
  <div class="abs service" style="left:509px">
    <svg width="104" height="112" viewBox="0 0 104 112"><path d="M52 4a48 48 0 0 1 12 94.5L52 110 40 98.5A48 48 0 0 1 52 4z" fill="#fff"/><circle cx="52" cy="52" r="43" fill="#2f9dcc"/><rect x="34" y="48" width="8" height="20" fill="#fff"/><path d="M45 48l8-16q5 0 4 8l-1 6h11q4 1 3 5l-3 14q-1 3-4 3H45z" fill="#fff"/></svg>
    <h3>BEST SUPPORT</h3><p>Nam libero tempore, cum soln obis est eligendi optio cum</p><div class="more">READ MORE&gt;&gt;</div>
  </div>
  <div class="abs service" style="left:716px">
    <svg width="104" height="112" viewBox="0 0 104 112"><path d="M52 4a48 48 0 0 1 12 94.5L52 110 40 98.5A48 48 0 0 1 52 4z" fill="#fff"/><circle cx="52" cy="52" r="43" fill="#2f9dcc"/><circle cx="45" cy="57" r="10" fill="none" stroke="#fff" stroke-width="7" stroke-dasharray="4 3.8"/><circle cx="45" cy="57" r="6" fill="#fff"/><circle cx="45" cy="57" r="2.5" fill="#2f9dcc"/><circle cx="62" cy="40" r="6" fill="none" stroke="#fff" stroke-width="5" stroke-dasharray="3 2.6"/><circle cx="63" cy="64" r="5" fill="none" stroke="#fff" stroke-width="4.5" stroke-dasharray="2.6 2.3"/></svg>
    <h3>BENEFITS</h3><p>Nam libero tempore, cum soln obis est eligendi optio cum</p><div class="more">READ MORE&gt;&gt;</div>
  </div>
  <div class="abs service" style="left:920px">
    <svg width="104" height="112" viewBox="0 0 104 112"><path d="M52 4a48 48 0 0 1 12 94.5L52 110 40 98.5A48 48 0 0 1 52 4z" fill="#fff"/><circle cx="52" cy="52" r="43" fill="#2f9dcc"/><text x="52" y="66" text-anchor="middle" font-family="Arimo, Arial, sans-serif" font-size="40" font-weight="700" fill="#fff">$</text></svg>
    <h3>COMPENSATION</h3><p>Nam libero tempore, cum soln obis est eligendi optio cum</p><div class="more">READ MORE&gt;&gt;</div>
  </div>
</section>

<section>
  <h2 class="abs section-title testi-title">CLIENT TESTIMONIALS</h2>
  <div class="abs quote"><b>&ldquo;</b> Neque porro quisquam est, qui dolorem ipsum quia dolor sit amet, consectet ur, adipisci velit, sed quia non numquam eius modi tempora inciduntt labore et dolore magnam aliquam quaerat voluptatem ullam corpo <b>&rdquo;</b></div>
  <svg class="abs" style="left:128px;top:1789px" width="30" height="34" viewBox="0 0 30 34"><path d="M1 0v33L29 0" fill="#fff" stroke="#cfd4d7"/><rect x="2" y="0" width="26" height="2" fill="#fff"/></svg>
  <div class="abs avatar" role="img" aria-label="Portrait of the client giving the testimonial"></div>
  <div class="abs client">- ALDO RENWICK</div>
  <div class="abs dots testi-dots"><span class="on"></span><span></span><span></span></div>
</section>

<section>
  <h2 class="abs section-title news-title">LATEST NEWS</h2>
  <svg class="abs news-arrows" width="36" height="22" viewBox="0 0 36 22"><path d="M12 3l-7 8 7 8M24 3l7 8-7 8" fill="none" stroke="#777" stroke-width="2"/></svg>

  <div class="abs news-item" style="top:1671px">
    <div class="news-thumb" role="img" aria-label="Photo of business colleagues in a meeting"></div>
    <div class="news-link">Sed ut perspiciatis unde omnis istit voluptatems antium doloremque laudantium rem</div>
    <div class="news-meta"><svg width="11" height="11"><rect x="0.5" y="1.5" width="10" height="9" fill="none" stroke="#0592cd"/><rect x="0" y="1" width="11" height="3" fill="#0592cd"/></svg>14/11/2015 &nbsp;| <svg width="11" height="11"><circle cx="5.5" cy="3" r="3" fill="#0592cd"/><path d="M0 11q5.5-8 11 0z" fill="#0592cd"/></svg>Mira Okafor</div>
  </div>
  <div class="abs news-item" style="top:1771px">
    <div class="news-thumb" role="img" aria-label="Photo of hands reviewing documents at a desk"></div>
    <div class="news-link">Sed ut perspiciatis unde omnis istit voluptatems antium doloremque laudantium rem</div>
    <div class="news-meta"><svg width="11" height="11"><rect x="0.5" y="1.5" width="10" height="9" fill="none" stroke="#0592cd"/><rect x="0" y="1" width="11" height="3" fill="#0592cd"/></svg>14/11/2015 &nbsp;| <svg width="11" height="11"><circle cx="5.5" cy="3" r="3" fill="#0592cd"/><path d="M0 11q5.5-8 11 0z" fill="#0592cd"/></svg>Mira Okafor</div>
  </div>
  <div class="abs news-item" style="top:1869px">
    <div class="news-thumb" role="img" aria-label="Photo of a team discussing around a table"></div>
    <div class="news-link">Sed ut perspiciatis unde omnis istit voluptatems antium doloremque laudantium rem</div>
    <div class="news-meta"><svg width="11" height="11"><rect x="0.5" y="1.5" width="10" height="9" fill="none" stroke="#0592cd"/><rect x="0" y="1" width="11" height="3" fill="#0592cd"/></svg>14/11/2015 &nbsp;| <svg width="11" height="11"><circle cx="5.5" cy="3" r="3" fill="#0592cd"/><path d="M0 11q5.5-8 11 0z" fill="#0592cd"/></svg>Mira Okafor</div>
  </div>
</section>

<footer>
  <div class="abs footer"></div>
  <h4 class="abs f-title" style="left:98px">ABOUT US</h4>
  <p class="abs f-text" style="left:98px;top:2053px;width:230px">Nemo enim ipsam voluptatem quia voluptas sit aspernatur aut odit aut fugit, sed quia consequuntur magni dolores eos qui ratione voluptatem sequi nesciunt.</p>

  <h4 class="abs f-title" style="left:366px">INFORMATION</h4>
  <ul class="abs f-links" style="left:366px;top:2053px"><li>Home</li><li>About us</li><li>Services</li><li>resources</li><li>Careers</li><li>Contact Us</li></ul>

  <h4 class="abs f-title" style="left:542px">NEWSLETTER SUBSCRIPTION</h4>
  <p class="abs f-text" style="left:542px;top:2053px;width:230px">Register your email address to get information about us</p>
  <div class="abs f-input">Email Address</div>
  <div class="abs btn f-btn">SUBSCRIBE</div>

  <h4 class="abs f-title" style="left:869px">CONTACT US</h4>
  <div class="abs f-contact" style="left:872px;top:2053px">
    <svg width="10" height="14" viewBox="0 0 10 14" style="margin-top:4px"><path d="M5 0a5 5 0 0 0-5 5c0 4 5 9 5 9s5-5 5-9a5 5 0 0 0-5-5z" fill="#fff"/><circle cx="5" cy="5" r="2" fill="#8b8b8b"/></svg>
    <span style="width:220px">At vero eos et accusamus et iusto od dignissimos ducimus qui blanditiis</span>
  </div>
  <div class="abs f-contact" style="left:871px;top:2120px">
    <svg width="13" height="13" viewBox="0 0 13 13" style="margin-top:4px"><path d="M2 0l3 3-1.5 2a7 7 0 0 0 4.5 4.5L10 8l3 3-2 2C5 12 1 8 0 2z" fill="#fff"/></svg>
    <span>1 800 555 0142</span>
  </div>
  <div class="abs f-contact" style="left:870px;top:2160px">
    <svg width="15" height="11" viewBox="0 0 15 11" style="margin-top:5px"><rect width="15" height="11" fill="#fff"/><path d="M0 0l7.5 6L15 0" fill="none" stroke="#8b8b8b"/></svg>
    <span style="text-decoration:underline">info@shiftpathways.example</span>
  </div>

  <div class="abs f-rule"></div>
  <p class="abs copyright">Copyright © 2015 Shift Pathways. All rights reserved.</p>
  <div class="abs social"><span></span><span></span><span></span><span></span></div>
</footer>

</body>
</html>
```